Pig club info pack flyers

We need base artwork to which we can add headings and content. we are looking for double sided A4 designs with blank Word suitable blocks which can hold content on topics including the law, research findings, zoonotic diseases etc etc.
We want them bright but not too complex nor too cartoonish. they object is to be eye-catching but credible. Colours should reflect our logo colours. The running pig line art, if used, should be the yellow in our logo. Maybe a standard heading such as THE FACTS. Open to all ideas.
Target Market(s)
Potential members, existing members, land managers
Industry/Entity Type
Conservation/hunting

```html
<!DOCTYPE html>
<html lang="en">
<head>
<meta charset="utf-8">
<title>The Facts – Info Pack Flyer</title>
<link href="https://fonts.googleapis.com/css2?family=Montserrat:wght@400;500;600;700;800&display=swap" rel="stylesheet">
<style>
  :root{
    --bg:#e8e6e7;
    --amber:#e39a3c;
    --amber-light:#efaa4f;
    --navy:#0f2a4e;
    --navy-light:#1d3f6e;
    --white:#ffffff;
    --rule:rgba(255,235,200,.55);
    --scene-mid:#6b6658;
    --scene-dark:#1f1f1c;
  }
  *{box-sizing:border-box;margin:0;padding:0}
  html,body{width:1200px;height:1200px;overflow:hidden;background:var(--bg);font-family:'Montserrat',sans-serif}
  .sheet{position:absolute;top:216px;width:552px;height:775px;overflow:hidden;
    background:linear-gradient(180deg,var(--amber) 0%,var(--amber-light) 55%,var(--amber) 100%);
    box-shadow:0 4px 14px rgba(0,0,0,.28)}
  .sheet--front{left:37px}
  .sheet--back{left:624px}
  .abs{position:absolute}
  .brand{left:0;right:0;top:36px;display:flex;flex-direction:column;align-items:center;gap:8px}
  .brand__dot{width:54px;height:54px;border-radius:50%;background:var(--navy)}
  .brand__name{color:var(--navy);font-weight:700;font-size:15px;text-align:center;width:220px;line-height:1.25}
  .title{left:0;right:0;top:146px;text-align:center;color:var(--navy);font-weight:800;font-size:44px;letter-spacing:.5px}
  .intro{left:15px;right:15px;top:211px;color:var(--white);font-weight:500;font-size:13px;line-height:16.3px;text-align:justify;text-align-last:center}
  .callout{left:82px;top:290px;width:383px;height:38px;border:1.5px solid var(--navy);border-radius:7px;
    background:var(--amber-light);box-shadow:0 5px 6px rgba(0,0,0,.3);color:var(--navy);
    font-weight:700;font-size:26px;display:flex;align-items:center;justify-content:center}
  .pill{left:50%;transform:translateX(-50%);width:183px;height:24px;border-radius:8px;
    background:linear-gradient(90deg,var(--navy) 0%,var(--navy-light) 50%,var(--navy) 100%);
    color:var(--white);font-weight:700;font-size:16.5px;display:flex;align-items:center;justify-content:center}
  .body{color:var(--navy);font-size:11.2px;line-height:14.5px;text-align:justify;text-align-last:center}
  .sheet--front .body{left:27px;right:29px}
  .sheet--back .body{left:29px;right:26px}
  .rule{height:1px;background:linear-gradient(90deg,transparent,var(--rule),transparent)}
  .sheet--front .rule{left:75px;right:70px}
  .sheet--back .rule{left:70px;right:70px}
  .scene{left:0;right:0;bottom:0}
  .scene--front{top:553px;background:linear-gradient(180deg,rgba(107,102,88,0) 0%,var(--scene-mid) 30%,var(--scene-dark) 62%)}
  .scene--back{top:534px;background:linear-gradient(180deg,rgba(107,102,88,0) 0%,var(--scene-mid) 22%,var(--scene-dark) 60%)}
  .contact-brand{left:86px;top:466px;width:114px;display:flex;flex-direction:column;align-items:center;gap:6px}
  .contact-brand .brand__dot{width:40px;height:40px}
  .contact-brand .brand__name{font-size:11px;width:114px}
  .contact-divider{left:223px;top:450px;width:2px;height:94px;background:var(--white)}
  .contact{left:251px;top:451px;color:var(--white)}
  .contact__heading{color:var(--navy);font-weight:700;font-size:16.5px;margin-bottom:6px}
  .contact__row{font-size:11.3px;line-height:18px;font-weight:500}
  .contact__row b{font-weight:700}
</style>
</head>
<body>

<section class="sheet sheet--front">
  <div class="brand abs">
    <span class="brand__dot"></span>
    <span class="brand__name">Southern Range Hunters Association</span>
  </div>
  <h1 class="title abs">THE FACTS</h1>
  <p class="intro abs">Lorem Ipsum is simply dummy text of the printing and typesetting industry. Lorem Ipsum has been the industry's standard dummy text ever since the 1500s, when an unknown printer took a galley of type and scrambled it to make a type specimen book.</p>
  <div class="callout abs">Lorem Ipsum dummy text</div>

  <h2 class="pill abs" style="top:346px">The Law</h2>
  <p class="body abs" style="top:378px">Lorem Ipsum is simply dummy text of the printing and typesetting industry. Lorem Ipsum has been the industry's standard dummy text ever since the 1500s, when an unknown printer took a galley of type and scrambled it to make a type specimen book.</p>
  <div class="rule abs" style="top:434px"></div>

  <h2 class="pill abs" style="top:455px">Research Findings</h2>
  <p class="body abs" style="top:487px">Lorem Ipsum is simply dummy text of the printing and typesetting industry. Lorem Ipsum has been the industry's standard dummy text ever since the 1500s, when an unknown printer took a galley of type and scrambled it to make a type specimen book.</p>

  <div class="scene scene--front abs" role="img" aria-label="Silhouetted bush landscape with trees and palms, and a running pig in yellow line art"></div>
</section>

<section class="sheet sheet--back">
  <h2 class="pill abs" style="top:19px">Zoonotic Diseases</h2>
  <p class="body abs" style="top:51px">Lorem Ipsum is simply dummy text of the printing and typesetting industry. Lorem Ipsum has been the industry's standard dummy text ever since the 1500s, when an unknown printer took a galley of type and scrambled it to make a type specimen book.</p>
  <div class="rule abs" style="top:105px"></div>

  <h2 class="pill abs" style="top:125px">The Law</h2>
  <p class="body abs" style="top:157px">Lorem Ipsum is simply dummy text of the printing and typesetting industry. Lorem Ipsum has been the industry's standard dummy text ever since the 1500s, when an unknown printer took a galley of type and scrambled it to make a type specimen book.</p>
  <div class="rule abs" style="top:214px"></div>

  <h2 class="pill abs" style="top:233px">Research Findings</h2>
  <p class="body abs" style="top:265px">Lorem Ipsum is simply dummy text of the printing and typesetting industry. Lorem Ipsum has been the industry's standard dummy text ever since the 1500s, when an unknown printer took a galley of type and scrambled it to make a type specimen book.</p>
  <div class="rule abs" style="top:322px"></div>

  <h2 class="pill abs" style="top:341px">Zoonotic Diseases</h2>
  <p class="body abs" style="top:373px">Lorem Ipsum is simply dummy text of the printing and typesetting industry. Lorem Ipsum has been the industry's standard dummy text ever since the 1500s, when an unknown printer took a galley of type and scrambled it to make a type specimen book.</p>
  <div class="rule abs" style="top:430px"></div>

  <div class="scene scene--back abs" role="img" aria-label="Silhouetted mountain range and bush trees at dusk"></div>

  <div class="contact-brand abs">
    <span class="brand__dot"></span>
    <span class="brand__name">Southern Range Hunters Association</span>
  </div>
  <div class="contact-divider abs"></div>
  <div class="contact abs">
    <h3 class="contact__heading">Contact Us:</h3>
    <p class="contact__row">Phone: <b>1300 555 019</b></p>
    <p class="contact__row">Website: <b>www.srha.org.au</b></p>
    <p class="contact__row">Email: <b>info@srha.org.au</b></p>
    <p class="contact__row">Mail: <b>PO Box 100, Kelvale QLD 4000</b></p>
  </div>
</section>

</body>
</html>
```